Meridian Rest Supply Needs Business Card

Looking for a very nice looking business card. Creative but not extravagant. We sell beds and pillows across the U.S. and need something professional but catchy. I have attached the logo.

Name : Dale Fenwick
Title : President
Phone : (800) 417-2964
Email: sleep@quorvana.com
Website: www.quorvana.com

Can be single-sided or double-sided
horizontal or vertical

Can use Blues/Greys

Target Market(s)

Mass Market

Industry/Entity Type

Retail

Contact Information for Business Card

Name : Dale Fenwick
Title : President
Phone : (800) 417-2964
Email: sleep@quorvana.com
Website: www.quorvana.com

Requirements
Must have
• Clean, Modern, Smooth
• Can use Blues/Greys
• On the other side without the information - have something simple like www.quorvana.com or our logo
Nice to have
• Surprise me
Should not have
• Nothing crazy, nothing cluttered

```html
<!DOCTYPE html>
<html lang="en">
<head>
<meta charset="utf-8">
<title>Meridian Rest Supply – Business Card</title>
<link href="https://fonts.googleapis.com/css2?family=Open+Sans:wght@300;400;600&display=swap" rel="stylesheet">
<style>
  :root {
    --backdrop: #232323;
    --card-white: #ffffff;
    --brand-blue: #2ea6d8;
    --text-grey: #4a4a4a;
    --rule-grey: #c9c9c9;
  }
  * { margin: 0; padding: 0; box-sizing: border-box; }
  html, body {
    width: 1200px;
    height: 987px;
    overflow: hidden;
    background: var(--backdrop);
    font-family: "Open Sans", Arial, sans-serif;
  }
  .canvas {
    position: relative;
    width: 1200px;
    height: 987px;
  }
  .card {
    position: absolute;
    width: 615px;
    height: 351px;
  }
  .card--front {
    left: 294px;
    top: 128px;
    background: var(--card-white);
  }
  .card--back {
    left: 292px;
    top: 507px;
    background: var(--brand-blue);
  }
  .wordmark {
    font-family: "Open Sans", Arial, sans-serif;
    font-weight: 300;
    line-height: 1;
    letter-spacing: 1px;
  }
  .card--front .wordmark {
    position: absolute;
    left: 66px;
    top: 120px;
    font-size: 48px;
    color: var(--brand-blue);
  }
  .divider {
    position: absolute;
    left: 321px;
    top: 103px;
    width: 1px;
    height: 150px;
    background: linear-gradient(to bottom, rgba(201,201,201,0), var(--rule-grey) 20%, var(--rule-grey) 80%, rgba(201,201,201,0));
  }
  .contact-block {
    position: absolute;
    left: 354px;
    top: 108px;
  }
  .contact-name {
    font-size: 21px;
    font-weight: 600;
    color: var(--brand-blue);
    line-height: 26px;
  }
  .contact-title {
    font-size: 16px;
    color: var(--text-grey);
    line-height: 22px;
  }
  .contact-list {
    list-style: none;
    margin-top: 12px;
  }
  .contact-list li {
    display: flex;
    align-items: center;
    font-size: 15.5px;
    color: var(--text-grey);
    line-height: 23.5px;
  }
  .contact-icon {
    width: 14px;
    height: 14px;
    margin-right: 10px;
    margin-left: 4px;
    flex: none;
  }
  .back-line {
    position: absolute;
    left: 0;
    right: 0;
    top: 150px;
    display: flex;
    justify-content: center;
    align-items: baseline;
    color: var(--card-white);
  }
  .back-line .wordmark {
    font-size: 62px;
  }
  .url-affix {
    font-size: 14px;
    font-weight: 400;
    letter-spacing: 3px;
  }
  .url-affix--pre { margin-right: 2px; }
  .url-affix--post { margin-left: 4px; }
</style>
</head>
<body>
<div class="canvas">
  <section class="card card--front">
    <div class="wordmark">quorvana</div>
    <div class="divider"></div>
    <div class="contact-block">
      <div class="contact-name">Dale Fenwick</div>
      <div class="contact-title">President</div>
      <ul class="contact-list">
        <li>
          <svg class="contact-icon" viewBox="0 0 24 24" aria-hidden="true">
            <path fill="#2ea6d8" d="M6.6 10.8a15.1 15.1 0 0 0 6.6 6.6l2.2-2.2c.3-.3.7-.4 1-.2 1.1.4 2.3.6 3.6.6.6 0 1 .4 1 1V20c0 .6-.4 1-1 1A17 17 0 0 1 3 4c0-.6.4-1 1-1h3.5c.6 0 1 .4 1 1 0 1.3.2 2.5.6 3.6.1.3 0 .7-.2 1z"/>
          </svg>
          (800) 417-2964
        </li>
        <li>
          <svg class="contact-icon" viewBox="0 0 24 24" aria-hidden="true">
            <rect x="2" y="5" width="20" height="14" rx="1" fill="#2ea6d8"/>
            <path d="M3 6l9 7 9-7" fill="none" stroke="#ffffff" stroke-width="1.6"/>
          </svg>
          sleep@quorvana.com
        </li>
        <li>
          <svg class="contact-icon" viewBox="0 0 24 24" aria-hidden="true">
            <circle cx="12" cy="12" r="10" fill="#2ea6d8"/>
            <path d="M7 8c2 0 3 1 3 3s-2 2-2 4M15 5c-1 2 0 3 2 4s2 3 1 5" fill="none" stroke="#ffffff" stroke-width="1.6"/>
          </svg>
          www.quorvana.com
        </li>
      </ul>
    </div>
  </section>

  <section class="card card--back">
    <div class="back-line">
      <span class="url-affix url-affix--pre">www.</span>
      <span class="wordmark">quorvana</span>
      <span class="url-affix url-affix--post">.com</span>
    </div>
  </section>
</div>
</body>
</html>
```